the theater production needs a poster design

we need a poster design for a theater drama in Seoul , South Korea.

the title : THE LANTERN'S HARBOR
BASED ON MARTIN HOLLOWAY'S BOOK

where:Haesol Stagehouse, Dalwon-Gu, Seoul
when:2022.1.1~OpenRun
Saturday 3PM, 63PM, Sunday 5pm, Monday 7:30pm

TICKET PRICE: $45

BOOK NOW
02 471 3096
BRIM TROUPE

Director Hyejin Pyo Composer Sora Baek, Sound Director Dong Ryu
Producer Woosik Nam

Target Market(s)

for Chiristan and others

Industry/Entity Type

Christian community and non Christian society

Colors
0094D4
00A9DD
6FCCEA
C7EBF8
E9F6FB

Requirements
Must have
• the main Character, pilgrim should should carry some burdens on his shoulder

```html
<!DOCTYPE html>
<html lang="en">
<head>
<meta charset="utf-8">
<title>The Lantern's Harbor — Theatre Poster</title>
<link href="https://fonts.googleapis.com/css2?family=Russo+One&family=Roboto+Condensed:wght@300;400&family=Arimo:ital,wght@0,400;0,700;1,700&display=swap" rel="stylesheet">
<style>
  :root {
    --page-bg: #e4e6e8;
    --blue-deep: #0094D4;
    --blue-mid: #00A9DD;
    --blue-soft: #6FCCEA;
    --blue-pale: #C7EBF8;
    --blue-mist: #E9F6FB;
    --white: #ffffff;
    --stone-dark: #2f2a22;
    --stone-mid: #6b5d45;
    --stone-light: #b3a07c;
  }
  * { margin: 0; padding: 0; box-sizing: border-box; }
  html, body {
    width: 1200px; height: 1200px; overflow: hidden;
    background: var(--page-bg);
  }
  .poster {
    position: absolute; left: 220px; top: 62px;
    width: 760px; height: 1075px;
    background: linear-gradient(180deg, var(--blue-deep) 0%, var(--blue-mid) 100%);
    color: var(--white);
    font-family: "Arimo", Arial, sans-serif;
  }
  .title-art { position: absolute; left: 0; top: 0; width: 760px; height: 500px; }
  .title-word {
    font-family: "Russo One", "Arial Black", sans-serif;
    fill: url(#stoneTone);
    stroke: var(--white); stroke-width: 4; paint-order: stroke;
  }
  .title-sub {
    position: absolute; left: 253px; top: 502px; width: 430px;
    font-family: "Russo One", "Arial Black", sans-serif;
    font-size: 88px; line-height: 80px; letter-spacing: 2px;
    text-align: right; white-space: nowrap;
  }
  .source-line {
    position: absolute; right: 71px; top: 600px;
    font-family: "Roboto Condensed", "Arial Narrow", sans-serif;
    font-weight: 300; font-size: 30px; letter-spacing: 0.5px;
    white-space: nowrap;
  }
  .schedule {
    position: absolute; left: 0; top: 676px; width: 760px;
    text-align: center; font-size: 21px; line-height: 30px;
  }
  .schedule .dates { font-weight: 700; }
  .ticket { position: absolute; left: 178px; top: 812px; width: 216px; height: 100px; }
  .ticket svg { position: absolute; inset: 0; }
  .ticket-text {
    position: absolute; inset: 0; display: flex; flex-direction: column;
    align-items: center; justify-content: center; color: var(--blue-mid);
  }
  .ticket-label { font-size: 21px; line-height: 24px; }
  .ticket-price { font-size: 31px; font-weight: 700; line-height: 34px; }
  .booking { position: absolute; left: 446px; top: 812px; font-size: 21px; line-height: 28px; }
  .booking-head { font-weight: 700; font-style: italic; margin-bottom: 4px; }
  .credits {
    position: absolute; left: 0; top: 964px; width: 760px;
    text-align: center; font-size: 16px; line-height: 32px;
  }
  .credit-role {
    background: var(--white); color: var(--blue-deep);
    padding: 0 3px; margin-right: 2px;
  }
</style>
</head>
<body>
<main class="poster">
  <svg class="title-art" viewBox="0 0 760 500" role="img" aria-label="Title lettering filled with a photograph of weathered ancient stone temple architecture">
    <defs>
      <linearGradient id="stoneTone" x1="0" y1="0" x2="1" y2="1">
        <stop offset="0" stop-color="var(--stone-light)"/>
        <stop offset="0.45" stop-color="var(--stone-mid)"/>
        <stop offset="1" stop-color="var(--stone-dark)"/>
      </linearGradient>
    </defs>
    <text class="title-word" transform="translate(132,269) rotate(-90)" x="0" y="0" font-size="88" textLength="207" lengthAdjust="spacingAndGlyphs">THE</text>
    <text class="title-word" x="199" y="269" font-size="296" textLength="489" lengthAdjust="spacingAndGlyphs">LANT</text>
    <text class="title-word" x="70" y="484" font-size="284" textLength="618" lengthAdjust="spacingAndGlyphs">ERN'S</text>
  </svg>

  <h1 class="title-sub">HARBOR</h1>
  <p class="source-line">BASED ON MARTIN HOLLOWAY'S BOOK</p>

  <section class="schedule">
    <p>Haesol Stagehouse, Dalwon-Gu, Seoul</p>
    <p class="dates">2022.1.1~OpenRun</p>
    <p>Saturday 3PM, 63PM, Sunday 5pm, Monday 7:30pm</p>
  </section>

  <div class="ticket">
    <svg viewBox="0 0 216 100" aria-hidden="true">
      <path fill="var(--white)" d="M0 8 Q18 0 36 8 T72 8 T108 8 T144 8 T180 8 T216 8 Q208 22 216 36 T216 64 T216 92 Q198 100 180 92 T144 92 T108 92 T72 92 T36 92 T0 92 Q8 78 0 64 T0 36 T0 8 Z"/>
    </svg>
    <div class="ticket-text">
      <span class="ticket-label">TICKET PRICE:</span>
      <span class="ticket-price">$45</span>
    </div>
  </div>

  <section class="booking">
    <p class="booking-head">BOOK NOW</p>
    <p>02 471 3096</p>
    <p>BRIM TROUPE</p>
  </section>

  <section class="credits">
    <p><span class="credit-role">Director</span>Hyejin Pyo <span class="credit-role">Composer</span>Sora Baek, <span class="credit-role">Sound Director</span>Dong Ryu</p>
    <p><span class="credit-role">Producer</span>Woosik Nam</p>
  </section>
</main>
</body>
</html>
```